Modern card design needed for building development company

We are looking for a sharp modern new look for our business cards.
We are a New Zealand based company called TKV Ventures NZ LTD that specialises in subdividing large sections, housing and commercial buildings.
We have attached a photo of the current logo and would like to see it improved somehow as it looks a bit dated.
We are open to any colours.

Target Market(s)

Investors, Property buyers

Industry/Entity Type

Investment

Contact Information for Business Card

TKV VENTURES NZ LTD
www.tkvventuresnz.co.nz

Howard Pennick
Phone +64 21 843 192
Email hdpennick@fernmail.co.nz

Font styles to use
Serif
Sans Serif

Colors
0792cd
33a6d7
85cae6
6b449b
886aae
f04a50
ec1f27
f37122
f68d4d

Requirements
Must have
• Please try and make the logo more modern or if you have a similar one we would like to see it.

```html
<!DOCTYPE html>
<html lang="en">
<head>
<meta charset="utf-8">
<title>TKV Ventures NZ LTD – Business Card</title>
<link rel="stylesheet" href="https://fonts.googleapis.com/css2?family=Cinzel:wght@500&family=Open+Sans:wght@400;700&display=swap">
<style>
  :root {
    --stage: #ecebe8;
    --card-white: #ffffff;
    --card-dark: #2a2a2a;
    --brand-red: #ec1f27;
    --ink-grey: #444444;
    --band-grey: #474747;
    --logo-light: #f2f2f2;
  }
  * { box-sizing: border-box; margin: 0; padding: 0; }
  html, body {
    width: 1200px; height: 900px; overflow: hidden;
    background: var(--stage);
  }
  .stage { position: relative; width: 1200px; height: 900px; }

  .card {
    position: absolute;
    width: 560px; height: 320px;
    box-shadow: 0 6px 18px rgba(0,0,0,.18);
    overflow: hidden;
  }

  /* Back side */
  .card--back { left: 560px; top: 100px; background: var(--card-dark); }
  .card--back .wordmark {
    position: absolute; left: 0; right: 0; top: 118px;
    display: flex; align-items: center; justify-content: center; gap: 14px;
  }
  .card--back .wordmark-square { width: 22px; height: 22px; background: var(--logo-light); }
  .card--back .wordmark-name {
    font-family: "Cinzel", serif; font-weight: 500;
    font-size: 34px; line-height: 1.05; color: var(--logo-light);
    text-align: center; letter-spacing: 1px;
  }

  /* Front side */
  .card--front { left: 80px; top: 470px; background: var(--card-white); }
  .card-bands { position: absolute; inset: 0; }
  .holder-name {
    position: absolute; left: 74px; top: 26px;
    font-family: "Open Sans", sans-serif; font-weight: 700;
    font-size: 17px; color: var(--brand-red); letter-spacing: .3px;
  }
  .contact-list {
    position: absolute; left: 30px; top: 122px; list-style: none;
    font-family: "Open Sans", sans-serif; font-size: 13px; color: var(--ink-grey);
  }
  .contact-list li { display: flex; align-items: center; gap: 10px; height: 20px; }
  .contact-icon { width: 11px; height: 11px; flex: none; }
  .card--front .wordmark {
    position: absolute; left: 300px; top: 122px; width: 240px;
    display: flex; align-items: center; gap: 12px;
  }
  .card--front .wordmark-square { width: 20px; height: 20px; background: var(--brand-red); flex: none; }
  .card--front .wordmark-name {
    font-family: "Cinzel", serif; font-weight: 500;
    font-size: 27px; line-height: 1.1; color: var(--ink-grey);
  }
</style>
</head>
<body>
<main class="stage">

  <section class="card card--back" aria-label="Card back">
    <div class="wordmark">
      <span class="wordmark-square"></span>
      <span class="wordmark-name">TKV VENTURES<br>NZ LTD</span>
    </div>
  </section>

  <section class="card card--front" aria-label="Card front">
    <svg class="card-bands" viewBox="0 0 560 320" width="560" height="320" aria-hidden="true">
      <polygon points="22,20 44,20 36,42 14,42" fill="var(--brand-red)"/>
      <polygon points="46,20 58,20 50,42 38,42" fill="var(--band-grey)"/>
      <polygon points="0,232 292,278 300,290 0,248" fill="var(--brand-red)"/>
      <polygon points="296,278 560,278 560,320 270,320" fill="var(--band-grey)"/>
    </svg>

    <h1 class="holder-name">HOWARD PENNICK</h1>

    <ul class="contact-list">
      <li>
        <svg class="contact-icon" viewBox="0 0 12 12" aria-hidden="true"><path d="M2 1l2 0 1 3-1.3 1a7 7 0 0 0 3.3 3.3L8 7l3 1v2c0 .6-.5 1-1 1A9 9 0 0 1 1 2c0-.5.4-1 1-1z" fill="var(--brand-red)"/></svg>
        +64 21 843 192
      </li>
      <li>
        <svg class="contact-icon" viewBox="0 0 12 12" aria-hidden="true"><rect x="0.5" y="2" width="11" height="8" fill="var(--brand-red)"/><path d="M1 2.5l5 4 5-4" stroke="#fff" stroke-width="1" fill="none"/></svg>
        HDPENNICK@FERNMAIL.CO.NZ
      </li>
      <li>
        <svg class="contact-icon" viewBox="0 0 12 12" aria-hidden="true"><circle cx="6" cy="6" r="5.5" fill="var(--brand-red)"/><path d="M1 6h10M6 .5c-2.5 3-2.5 8 0 11M6 .5c2.5 3 2.5 8 0 11" stroke="#fff" stroke-width=".8" fill="none"/></svg>
        WWW.TKVVENTURESNZ.CO.NZ
      </li>
    </ul>

    <div class="wordmark">
      <span class="wordmark-square"></span>
      <span class="wordmark-name">TKV VENTURES<br>NZ LTD</span>
    </div>
  </section>

</main>
</body>
</html>
```